Business Card Design

We need a business card design for a kids clothes shop in Ireland called "Zest2Tots". Would prefer the colours Lime Green and Dark Purple to be used but are open to suggestions. The logo should include a "Cool" penguin with clothes on.

Shop

Zest2Tots
Harlows Complex,
Ashgrove Road, Childrenswear 0-12yrs
Ballykerrin,
XR28 4QW. Niamh Dolan.

```html
<!DOCTYPE html>
<html lang="en">
<head>
<meta charset="utf-8">
<title>Zest2Tots – Business Card</title>
<link href="https://fonts.googleapis.com/css2?family=Open+Sans:wght@400;600;700;800&display=swap" rel="stylesheet">
<style>
  :root {
    --purple: #5e0f63;
    --purple-light: #7a1d80;
    --purple-deep: #4a0a4f;
    --lime: #a6d13b;
    --white: #ffffff;
    --page: #ece8e3;
    --art-white: #f4f2f2;
    --art-grey: #dcd8d8;
  }
  * { box-sizing: border-box; margin: 0; padding: 0; }
  html, body {
    width: 1200px; height: 1023px; overflow: hidden;
    background: var(--page);
    font-family: "Open Sans", Arial, sans-serif;
  }
  .sheet {
    position: relative; width: 1200px; height: 1023px;
    display: flex; flex-direction: column; align-items: center; justify-content: center; gap: 70px;
  }
  .card {
    position: relative; width: 660px; height: 377px;
    border-radius: 22px; overflow: hidden;
    background: radial-gradient(ellipse at 40% 35%, var(--purple-light), var(--purple) 55%, var(--purple-deep));
    box-shadow: 0 10px 28px rgba(60, 20, 60, 0.25);
  }

  /* Front */
  .card-front .holder {
    position: absolute; left: 56px; top: 150px;
  }
  .holder-name {
    color: var(--lime); font-weight: 700; font-size: 24px; letter-spacing: 0.5px; text-transform: uppercase;
  }
  .holder-role {
    color: var(--white); font-size: 14px; margin-top: 4px; padding-left: 70px;
  }
  .mascot-art {
    position: absolute; right: 0; bottom: 0; width: 300px; height: 250px;
    border-top-left-radius: 150px;
    background: linear-gradient(160deg, var(--art-white), var(--art-grey));
  }

  /* Back */
  .brand {
    position: absolute; left: 36px; top: 128px; width: 290px;
  }
  .brand-name {
    display: flex; align-items: center; gap: 8px;
    color: var(--lime); font-weight: 800; font-size: 46px; line-height: 1; letter-spacing: -1px;
    white-space: nowrap;
  }
  .brand-dot {
    width: 20px; height: 20px; border-radius: 50%; background: var(--white); flex: none;
  }
  .brand-tagline {
    color: var(--lime); font-weight: 600; font-size: 12px; letter-spacing: 0.5px;
    text-transform: uppercase; margin-top: 10px; padding-left: 28px;
  }
  .divider {
    position: absolute; left: 340px; top: 56px; width: 2px; height: 265px; background: var(--lime);
  }
  .contact {
    position: absolute; left: 362px; top: 78px; width: 272px;
    display: flex; flex-direction: column; gap: 12px;
  }
  .contact-line {
    display: flex; align-items: center; justify-content: space-between; gap: 10px;
    color: var(--white); font-size: 15px;
  }
  .contact-icon { width: 18px; height: 18px; flex: none; }
  .address {
    margin-top: 34px; color: var(--lime); font-size: 13px; line-height: 1.55; letter-spacing: 0.2px;
    text-transform: uppercase; white-space: nowrap;
  }
</style>
</head>
<body>
<main class="sheet">

  <section class="card card-front" aria-label="Business card front">
    <div class="holder">
      <p class="holder-name">Niamh Dolan</p>
      <p class="holder-role">Director</p>
    </div>
    <div class="mascot-art" role="img" aria-label="Illustration of the shop's cartoon penguin mascot peeking in from the corner"></div>
  </section>

  <section class="card card-back" aria-label="Business card back">
    <div class="brand">
      <p class="brand-name"><span class="brand-dot"></span>Zest2Tots</p>
      <p class="brand-tagline">Childrenswear 0-12yrs</p>
    </div>
    <div class="divider"></div>
    <div class="contact">
      <p class="contact-line">01559307418
        <svg class="contact-icon" viewBox="0 0 18 18" aria-hidden="true"><circle cx="9" cy="9" r="9" fill="var(--lime)"/><path d="M6 5.5c0 4 2.5 6.5 6.5 6.5l.8-1.6-1.8-.9-.8.8c-1.2-.5-2-1.3-2.5-2.5l.8-.8-.9-1.8z" fill="var(--purple)"/></svg>
      </p>
      <p class="contact-line">07961538207
        <svg class="contact-icon" viewBox="0 0 18 18" aria-hidden="true"><circle cx="9" cy="9" r="9" fill="var(--lime)"/><rect x="6.5" y="4" width="5" height="10" rx="1" fill="var(--purple)"/></svg>
      </p>
      <p class="contact-line">niamh@Zest2Tots.com
        <svg class="contact-icon" viewBox="0 0 18 18" aria-hidden="true"><circle cx="9" cy="9" r="9" fill="var(--lime)"/><rect x="4.5" y="6" width="9" height="6.5" fill="var(--purple)"/><path d="M4.5 6l4.5 3.5L13.5 6" stroke="var(--lime)" fill="none"/></svg>
      </p>
      <p class="address">Harlows Complex, Ashgrove Road<br>Ballykerrin, XR28 4QW</p>
    </div>
  </section>

</main>
</body>
</html>
```